Industrial Professional Business Card Design (Vantrel KX)

Would like professional looking business cards. Not too busy leaning towards minimal. Should have a slogan like:
"Industrial Automation and Control".

We are a tech company that programs industrial PLC computers. We also develop custom hardware solutions. Please use the logo for inspiration.

Target Market(s)

Mining, industrial, processing, automation, factory

Industry/Entity Type

Engineering

Contact Information for Business Card

Name, phone, email, website. job title.

Font styles to use
Other font styles liked:
• droid sans

Requirements
Must have
• Use colours that go well with the logo. Not too busy design.

```html
<!DOCTYPE html>
<html lang="en">
<head>
<meta charset="utf-8">
<title>Vantrel KX – Business Card</title>
<link rel="stylesheet" href="https://fonts.googleapis.com/css2?family=Noto+Sans:wght@400;700&display=swap">
<style>
  :root {
    --backdrop: #3a3a3c;
    --card: #262628;
    --silver: #9a9ca0;
    --orange: #f26b1d;
    --blue-deep: #1d3f7a;
    --blue: #2a78b8;
    --brand-blue: #2f9be0;
    --white: #ffffff;
  }
  * { box-sizing: border-box; margin: 0; padding: 0; }
  html, body {
    width: 799px; height: 1200px; overflow: hidden;
    background: var(--backdrop);
    font-family: "Noto Sans", sans-serif;
  }
  .card {
    position: absolute; left: 80px; width: 640px; height: 366px;
    background: var(--card); border-radius: 6px; overflow: hidden;
    box-shadow: 0 10px 24px rgba(0,0,0,.45);
  }
  .card--front { top: 117px; }
  .card--back { top: 717px; }
  .card__art { position: absolute; inset: 0; width: 640px; height: 366px; }

  /* Front */
  .front__brand {
    position: absolute; top: 120px; left: 0; right: 0;
    display: flex; align-items: center; justify-content: center; gap: 16px;
  }
  .brand__dot { width: 46px; height: 46px; border-radius: 50%; background: var(--silver); }
  .front__name { font-size: 54px; font-weight: 400; color: var(--silver); letter-spacing: 1px; }
  .front__web { position: absolute; left: 24px; top: 286px; font-size: 15px; color: var(--white); }
  .front__slogan { position: absolute; right: 26px; top: 328px; font-size: 17px; color: var(--white); }

  /* Back */
  .back__brand { position: absolute; top: 26px; left: 28px; display: flex; align-items: center; gap: 16px; }
  .back__dot { width: 52px; height: 52px; border-radius: 50%; background: var(--orange); }
  .back__name { font-size: 44px; font-weight: 400; color: var(--brand-blue); }
  .contact { position: absolute; top: 104px; left: 30px; list-style: none; font-size: 14.5px; color: var(--white); line-height: 21px; }
  .contact li { display: flex; align-items: center; gap: 9px; }
  .contact__address { margin-left: 0; }
  .contact svg { width: 13px; height: 13px; flex: none; }
  .person { position: absolute; right: 30px; bottom: 30px; text-align: right; color: var(--white); }
  .person__name { font-size: 25px; font-weight: 700; }
  .person__title { font-size: 16px; }
</style>
</head>
<body>

<section class="card card--front">
  <svg class="card__art" viewBox="0 0 640 366" aria-hidden="true">
    <rect x="0" y="318" width="330" height="9" fill="var(--orange)"/>
    <defs>
      <linearGradient id="frontBand" x1="0" x2="1" y1="0" y2="0">
        <stop offset="0" stop-color="var(--blue-deep)"/>
        <stop offset="1" stop-color="var(--blue)"/>
      </linearGradient>
      <linearGradient id="backBand" x1="0" x2="1" y1="0" y2="0">
        <stop offset="0" stop-color="var(--blue-deep)"/>
        <stop offset="1" stop-color="var(--blue)"/>
      </linearGradient>
    </defs>
    <path d="M290 366 C300 330 310 312 345 312 L640 312 L640 366 Z" fill="url(#frontBand)"/>
  </svg>
  <div class="front__brand">
    <span class="brand__dot"></span>
    <span class="front__name">Vantrel KX</span>
  </div>
  <p class="front__web">www.vantrelkx.com</p>
  <p class="front__slogan">Automation &amp; Control Solutions</p>
</section>

<section class="card card--back">
  <svg class="card__art" viewBox="0 0 640 366" aria-hidden="true">
    <path d="M0 232 C150 300 300 330 430 322 C530 316 600 300 640 288 L640 366 L0 366 Z" fill="url(#backBand)"/>
    <path d="M0 250 C160 300 320 312 640 296" fill="none" stroke="var(--card)" stroke-width="14"/>
    <path d="M0 212 C150 300 320 318 640 268" fill="none" stroke="var(--orange)" stroke-width="8"/>
  </svg>
  <div class="back__brand">
    <span class="back__dot"></span>
    <span class="back__name">Vantrel KX</span>
  </div>
  <ul class="contact">
    <li class="contact__address">48 Foundry Rd., Millbrook, US 204518</li>
    <li>
      <svg viewBox="0 0 16 16"><path fill="var(--orange)" d="M3 1h3l1.5 4-2 1.3a9 9 0 0 0 4.2 4.2L11 8.5l4 1.5v3a2 2 0 0 1-2 2A12 12 0 0 1 1 3a2 2 0 0 1 2-2z"/></svg>
      555-014-2270
    </li>
    <li>
      <svg viewBox="0 0 16 16"><rect x="1" y="3" width="14" height="10" rx="1" fill="var(--orange)"/><path d="M1.5 4 8 9l6.5-5" fill="none" stroke="var(--card)" stroke-width="1.3"/></svg>
      daniel@vantrelkx.com
    </li>
    <li>
      <svg viewBox="0 0 16 16"><circle cx="8" cy="8" r="7" fill="var(--orange)"/><path d="M1 8h14M8 1c-3 3.5-3 10.5 0 14M8 1c3 3.5 3 10.5 0 14" fill="none" stroke="var(--card)" stroke-width="1"/></svg>
      www.vantrelkx.com
    </li>
  </ul>
  <div class="person">
    <p class="person__name">Daniel Marsh</p>
    <p class="person__title">Managing Director</p>
  </div>
</section>

</body>
</html>
```